BPH Business Card 2018

Brellmore Chiropractic. We have two locations that we want to advertise on the same card. Calderwick OrthoAxis campus address: 3815 Pemberly Dr., Suite 240, Flowood, MS 39587. Madison address: 426 Larkmoor Dr., Building D., Madison, MS 39674. website: www.drbrellmore.example. o:(601)555-0148 f:(601)555-0173

Target Market(s)

Health care decision makers: primary care doctors and mothers

Contact Information for Business Card

I have no idea; up for any suggestions and I'd do much better picking from examples versus describing what I'm looking for. We are in a very high end location and would like the cards to look really sharp.

Requirements
Must have
• My name, Tobias R Venmark, D.C.

```html
<!DOCTYPE html>
<html lang="en">
<head>
<meta charset="utf-8">
<title>Brellmore Chiropractic – Business Card</title>
<link href="https://fonts.googleapis.com/css2?family=Tinos:wght@400;700&display=swap" rel="stylesheet">
<style>
  :root {
    --brand-blue: #2e3192;
    --brand-blue-light: #3454a8;
    --ink: #111111;
    --paper: #ffffff;
  }
  * { margin: 0; padding: 0; box-sizing: border-box; }
  html, body {
    width: 1200px;
    height: 900px;
    overflow: hidden;
    background: var(--paper);
    font-family: "Tinos", "Times New Roman", serif;
  }
  .sheet {
    position: relative;
    width: 1200px;
    height: 900px;
  }

  /* Back side: brand panel */
  .card-back {
    position: absolute;
    left: 0;
    top: 0;
    width: 540px;
    height: 900px;
    background: radial-gradient(circle at 272px 464px, var(--brand-blue-light) 0%, var(--brand-blue) 62%);
    overflow: hidden;
  }
  .card-back__content {
    position: absolute;
    left: 0;
    top: 0;
    width: 900px;
    height: 540px;
    transform-origin: top left;
    transform: translateX(540px) rotate(90deg);
  }
  .card-back__wordmark {
    position: absolute;
    left: 276px;
    top: 190px;
    color: var(--paper);
    font-weight: 400;
    line-height: 1;
  }
  .card-back__wordmark .wordmark__name {
    display: block;
    font-size: 98px;
    letter-spacing: 1px;
  }
  .card-back__wordmark .wordmark__trade {
    display: block;
    font-size: 62px;
    letter-spacing: 2px;
    margin-top: 6px;
  }

  /* Front side: contact details */
  .card-front {
    position: absolute;
    left: 540px;
    top: 0;
    width: 660px;
    height: 900px;
    background: var(--paper);
    overflow: hidden;
  }
  .card-front__content {
    position: absolute;
    left: 0;
    top: 0;
    width: 900px;
    height: 660px;
    transform-origin: top left;
    transform: translateX(660px) rotate(90deg);
  }
  .card-front__wordmark {
    position: absolute;
    left: 224px;
    top: 108px;
    color: var(--brand-blue);
    font-weight: 400;
    line-height: 1;
  }
  .card-front__wordmark .wordmark__name {
    display: block;
    font-size: 64px;
    letter-spacing: 1px;
  }
  .card-front__wordmark .wordmark__trade {
    display: block;
    font-size: 40px;
    letter-spacing: 1.5px;
    margin-top: 2px;
  }
  .practitioner {
    position: absolute;
    left: 224px;
    top: 272px;
    font-size: 34px;
    font-weight: 700;
    color: var(--ink);
  }
  .contact-list {
    position: absolute;
    left: 104px;
    top: 332px;
    list-style: none;
    font-size: 25px;
    line-height: 36px;
    color: var(--ink);
  }
  .contact-list .label {
    display: inline-block;
    width: 40px;
    font-weight: 700;
    color: var(--brand-blue);
  }
  .contact-list .sep { margin-right: 10px; }
  .contact-list .inline-label {
    font-weight: 700;
    color: var(--brand-blue);
  }
</style>
</head>
<body>
<main class="sheet">
  <section class="card-back" aria-label="Card back">
    <div class="card-back__content">
      <div class="card-back__wordmark">
        <span class="wordmark__name">BRELLMORE</span>
        <span class="wordmark__trade">CHIROPRACTIC</span>
      </div>
    </div>
  </section>

  <section class="card-front" aria-label="Card front">
    <div class="card-front__content">
      <div class="card-front__wordmark">
        <span class="wordmark__name">BRELLMORE</span>
        <span class="wordmark__trade">CHIROPRACTIC</span>
      </div>
      <h1 class="practitioner">Tobias R Venmark, D.C.</h1>
      <ul class="contact-list">
        <li><span class="label">A1</span><span class="sep">:</span>3815 Pemberly Dr., Suite 240, Flowood, MS 39587</li>
        <li><span class="label">A2</span><span class="sep">:</span>426 Larkmoor Dr., Building D., Madison, MS 39674</li>
        <li><span class="label">W</span><span class="sep">:</span>drbrellmore.example</li>
        <li><span class="label">O</span><span class="sep">:</span>(601)555-0148 | <span class="inline-label">F</span> : (601)555-0173</li>
      </ul>
    </div>
  </section>
</main>
</body>
</html>
```